Boutique High End Custom Furniture Store, Client Appreciation Card

We are looking to create a 5 x 7 card for our best clients that offer a 15% discount on their next furniture purchase. We would like to use both sides, full colour.

We are a high-end boutique furniture store located in Calgary, AB, Canada.

I have attached a card we did for our grand reopening that we like -- it's fresh with lots of white space. I have attached the image we used as well as a possible second image of furniture.

I have also attached other examples -- all seem fresh and clean with a layer of luxury.

I have attached all versions of our logo in an EPS file.

Target Market(s)

High disposable income, women over 40 who love style, contemporary design and fine art. Think Lina Morrow, Finch Allard, Vera Quill perfume and http://www.marlowbey.example/

Industry/Entity Type

Boutique

Font styles to use
Sans Serif
Script

Colors
33a6d7
0592cd
85cae6
eda3c7
e667a6

Requirements
Must have
• Must be colour on both side (one side logo perhaps), the other side has content? Card needs to be 5 x 7 (either orientation is okay). Card needs to be fresh, stylish and current with the use of colour i.e. not all black and white. Logo needs to be prominent on either side.
• Please also have a look at our website.
Should not have
• Should not feel traditional or dated but at the same time not too playful so that it looks unprofessional. We are not "Hal's discount Sofas"!

```html
<!DOCTYPE html>
<html lang="en">
<head>
<meta charset="utf-8">
<title>Larkspur Home – Client Appreciation Card</title>
<link rel="stylesheet" href="https://fonts.googleapis.com/css2?family=Josefin+Sans:wght@200;300;400&family=Lato:wght@300;400&display=swap">
<style>
  :root {
    --backdrop: #d9d1d4;
    --blush: #deb0bb;
    --blush-deep: #c98d9c;
    --white: #ffffff;
    --veil: rgba(255, 255, 255, 0.82);
    --wall: #eeeceb;
    --wood: #b7a99c;
    --floor: #cfcac6;
  }
  * { box-sizing: border-box; margin: 0; padding: 0; }
  html, body { width: 1200px; height: 952px; overflow: hidden; }
  body {
    background: var(--backdrop);
    position: relative;
    font-family: "Lato", sans-serif;
  }
  .card {
    position: absolute;
    box-shadow: 0 10px 30px rgba(60, 40, 50, 0.18);
    overflow: hidden;
  }

  /* Offer side */
  .card--offer {
    left: 480px; top: 56px;
    width: 670px; height: 478px;
    background: var(--blush);
  }
  .offer__photo {
    position: absolute; left: 0; top: 0;
    width: 330px; height: 100%;
    background: linear-gradient(180deg, var(--wall) 0%, #e4dfdc 55%, var(--floor) 100%);
  }
  .offer__fade {
    position: absolute; left: 180px; top: 0;
    width: 170px; height: 100%;
    background: linear-gradient(90deg, rgba(222,176,187,0) 0%, var(--blush) 100%);
  }
  .offer__frame {
    position: absolute; left: 200px; top: 22px;
    width: 446px; height: 432px;
    border: 1px solid var(--white);
  }
  .offer__content {
    position: absolute; left: 236px; top: 40px;
    width: 396px;
    color: var(--white);
    text-align: center;
  }
  .offer__lead {
    font-family: "Josefin Sans", sans-serif;
    font-weight: 300;
    font-size: 34px;
    letter-spacing: 4px;
  }
  .offer__enjoy {
    font-family: "Josefin Sans", sans-serif;
    font-weight: 300;
    font-size: 17px;
    letter-spacing: 6px;
    margin-top: 4px;
  }
  .offer__deal {
    display: flex; align-items: center; justify-content: center;
    gap: 12px; margin-top: 4px;
  }
  .offer__percent {
    font-family: "Josefin Sans", sans-serif;
    font-weight: 200;
    font-size: 124px;
    line-height: 1;
    color: transparent;
    -webkit-text-stroke: 2px var(--white);
  }
  .offer__off {
    font-family: "Josefin Sans", sans-serif;
    font-weight: 300;
    font-size: 48px;
    line-height: 0.95;
    text-align: left;
  }
  .offer__name {
    font-family: "Josefin Sans", sans-serif;
    font-weight: 300;
    font-size: 32px;
    letter-spacing: 2px;
    margin-top: 6px;
  }
  .offer__about {
    font-size: 13.5px;
    line-height: 1.5;
    margin-top: 12px;
    text-align: left;
  }
  .offer__terms {
    font-size: 10px;
    margin-top: 8px;
    text-align: left;
  }
  .offer__contact {
    font-size: 11px;
    letter-spacing: 0.6px;
    line-height: 1.7;
    margin-top: 6px;
    text-align: left;
    white-space: nowrap;
  }
  .offer__contact .dot {
    display: inline-block; width: 6px; height: 6px;
    border: 1px solid var(--white); border-radius: 50%;
    margin: 0 6px; vertical-align: middle;
  }

  /* Brand side */
  .card--brand {
    left: 28px; top: 483px;
    width: 614px; height: 438px;
  }
  .brand__photo {
    position: absolute; inset: 0;
    background: linear-gradient(180deg, var(--wall) 0%, #e6e2de 45%, var(--wood) 70%, var(--floor) 100%);
  }
  .brand__panel {
    position: absolute; left: 150px; top: 122px;
    width: 332px; height: 196px;
    background: var(--veil);
    border: 1px solid var(--white);
  }
  .brand__panel::after {
    content: ""; position: absolute; inset: 8px;
    border: 1px solid rgba(190, 175, 170, 0.6);
  }
  .brand__lockup {
    position: absolute; inset: 0;
    display: flex; flex-direction: column; align-items: center; justify-content: center;
    gap: 8px; padding-top: 14px;
  }
  .brand__square {
    width: 22px; height: 22px;
    border: 1px solid var(--blush-deep);
    margin-bottom: 12px;
  }
  .brand__name {
    font-family: "Lato", sans-serif;
    font-weight: 300;
    font-size: 26px;
    letter-spacing: 1px;
    color: var(--blush-deep);
  }
  .brand__tagline {
    font-family: "Lato", sans-serif;
    font-weight: 300;
    font-size: 11px;
    letter-spacing: 2px;
    color: var(--blush-deep);
  }
</style>
</head>
<body>
  <section class="card card--offer">
    <div class="offer__photo" role="img" aria-label="Photo of a white room with a pale sideboard, a dark chair and a yellow vase of white calla lilies"></div>
    <div class="offer__fade"></div>
    <div class="offer__frame"></div>
    <div class="offer__content">
      <p class="offer__lead">our gift to you</p>
      <p class="offer__enjoy">– ENJOY –</p>
      <div class="offer__deal">
        <span class="offer__percent">15%</span>
        <span class="offer__off">OFF<br>AT</span>
      </div>
      <h2 class="offer__name">Larkspur Home</h2>
      <p class="offer__about">Larkspur Home is a unique boutique custom furniture store offering a wide selection of furniture, rugs, bedding, lighting, window coverings, accessories and interior design services.</p>
      <p class="offer__terms">Offer is good for one-time use and cannot be combined with other offers.</p>
      <p class="offer__contact">482 LARCH AVE SW, CALGARY AB<span class="dot"></span>403.555.0182<br>INFO@LARKSPURHOME.EXAMPLE<span class="dot"></span>LARKSPURHOME.EXAMPLE</p>
    </div>
  </section>

  <section class="card card--brand">
    <div class="brand__photo" role="img" aria-label="Photo of a modern sideboard with a framed painting, a dark tower sculpture, a yellow vase of lilies, a chair and a leather bench"></div>
    <div class="brand__panel">
      <div class="brand__lockup">
        <span class="brand__square"></span>
        <h1 class="brand__name">Larkspur Home</h1>
        <p class="brand__tagline">Bespoke Furniture Atelier</p>
      </div>
    </div>
  </section>
</body>
</html>
```